Professional Photography Business cards

I need business cards that include my logo which I have uploaded. I run a photography business. I am open to ideas but I would like one side to have my logo and the other side to have my contact info. I don't have a website made but I do own a website domain. I have uploaded 2 different logo color schemes. My business colors are Blue, black , and white.

Business Name
Business Phone Number
Business Email
Business Website address
Instagram

Industry/Entity Type

Professional Photography

Contact Information for Business Card

Phone Number: 555-314-8027 email: info@tkellan-studios.example Instagram: @t.kellanstudios website doman- www.tkellan-studios.example

Requirements
Must have
• I like the idea of a business card with a full black background front and back of card. My colors must include royal blue, black, and white

```html
<!DOCTYPE html>
<html lang="en">
<head>
<meta charset="utf-8">
<title>T. Kellan Studios – Business Cards</title>
<link rel="stylesheet" href="https://fonts.googleapis.com/css2?family=Montserrat:wght@400;500;700&display=swap">
<style>
  :root {
    --royal-blue: #1b27b8;
    --deep-blue: #0a0f86;
    --ink: #111111;
    --paper: #ffffff;
    --backdrop: #e9eaee;
  }
  * { box-sizing: border-box; margin: 0; padding: 0; }
  html, body {
    width: 1200px; height: 912px; overflow: hidden;
    background: var(--backdrop);
    font-family: "Montserrat", sans-serif;
  }
  .canvas { position: relative; width: 1200px; height: 912px; }

  .card {
    position: absolute;
    width: 640px; height: 366px;
    border-radius: 26px;
    overflow: hidden;
    background: linear-gradient(135deg, var(--royal-blue) 0%, var(--deep-blue) 100%);
    box-shadow: 0 10px 28px rgba(0, 0, 0, 0.22);
  }
  .card--front { left: 70px; top: 60px; }
  .card--back  { left: 490px; top: 486px; }

  /* Front side */
  .brand-mark {
    position: absolute; inset: 0;
    display: flex; align-items: center; justify-content: center; gap: 18px;
  }
  .brand-mark__dot {
    width: 54px; height: 54px; border-radius: 50%;
    border: 3px solid var(--paper);
  }
  .brand-mark__name {
    color: var(--paper);
    font-weight: 500; font-size: 40px; letter-spacing: 1px;
  }

  /* Back side */
  .back-shape { position: absolute; inset: 0; }
  .back-logo {
    position: absolute; left: 400px; top: 88px; width: 220px;
    text-align: center;
    color: var(--royal-blue);
    font-weight: 500; font-size: 28px; line-height: 1.2;
  }
  .holder { position: absolute; left: 58px; top: 140px; color: var(--paper); }
  .holder__name { font-weight: 700; font-size: 27px; letter-spacing: 1.5px; white-space: nowrap; }
  .holder__role { font-weight: 400; font-size: 17px; margin-top: 2px; }

  .contact-list {
    position: absolute; left: 160px; top: 262px;
    list-style: none; color: var(--paper);
    font-size: 15px; font-weight: 400;
  }
  .contact-list li { display: flex; align-items: center; gap: 8px; height: 22px; white-space: nowrap; }
  .contact-list svg { width: 13px; height: 13px; flex: none; }
  .contact-list .plain-dot {
    width: 11px; height: 11px; border-radius: 2px; background: var(--paper); flex: none; margin: 0 1px;
  }
</style>
</head>
<body>
<main class="canvas">

  <section class="card card--front" aria-label="Card front">
    <div class="brand-mark">
      <span class="brand-mark__dot"></span>
      <span class="brand-mark__name">T. Kellan Studios</span>
    </div>
  </section>

  <section class="card card--back" aria-label="Card back">
    <svg class="back-shape" viewBox="0 0 640 366" width="640" height="366" aria-hidden="true">
      <circle cx="490" cy="92" r="190" fill="#111111"/>
      <circle cx="502" cy="82" r="188" fill="#ffffff"/>
    </svg>

    <div class="back-logo">T. Kellan<br>Studios</div>

    <div class="holder">
      <p class="holder__name">THEO KELLAN</p>
      <p class="holder__role">Founder</p>
    </div>

    <ul class="contact-list">
      <li>
        <svg viewBox="0 0 16 16" aria-hidden="true"><path fill="#fff" d="M3.6 1.5l2.2 2.6-1.3 1.7c.9 2 2.7 3.8 4.7 4.7l1.7-1.3 2.6 2.2-1.2 2.3C7 15.4.6 9 1.3 2.7z"/></svg>
        555-314-8027
      </li>
      <li>
        <svg viewBox="0 0 16 16" aria-hidden="true"><rect x="1.5" y="3.5" width="13" height="9" fill="none" stroke="#fff" stroke-width="1.5"/><path d="M1.5 3.5L8 9l6.5-5.5" fill="none" stroke="#fff" stroke-width="1.5"/></svg>
        info@tkellan-studios.example
      </li>
      <li>
        <span class="plain-dot"></span>
        @t.kellanstudios
      </li>
      <li>
        <svg viewBox="0 0 16 16" aria-hidden="true"><g fill="none" stroke="#fff" stroke-width="1.3"><circle cx="8" cy="8" r="6.3"/><ellipse cx="8" cy="8" rx="2.8" ry="6.3"/><path d="M1.7 8h12.6"/></g></svg>
        www.tkellan-studios.example
      </li>
    </ul>
  </section>

</main>
</body>
</html>
```